Website for premium health insurance and concierge medicine

This is a brand new website for Vantor Insurance Services that specializes in Health Insurance and Concierge Medicine for high net-worth and affluent individuals and families. Through this website, clients will be able to learn about products and services, submit applications, and complete self enrollment forms. The website needs to have a premium look & feel that will appeal to a discerning high net-worth individual.

I’m looking for 4 pages in total to begin with. I’m also looking for a designer who will be interested in continuing to build out this new site further over the next few months.

The headline for each page is listed below:

Page 1: HOME PAGE
“Premium Healthcare | Bespoke Concierge Services | Absolute Peace of Mind.”

Page 2: HEALTH INSURANCE
“Premium Healthcare | Elevated.”

Page 3: CONCIERGE MEDICINE
“Personalized Medicine | At-Home Concierge Care | Your Private Physician, 24/7.”

Page 4: DENTAL & VISION
“Your Smile | Your Vision | Perfected.”

Here are several links to existing websites that can be used as design inspiration:

https://brevanwell.com
https://www.quemby.org/specialties-services/other-programs-services/concierge-medicine
https://physelmdkx.com

More generally speaking, I like a clean, modern, dutch style of websites. Here’s an unrelated site that has a good design:

https://www.ostravine.com

Here are a few additional phrases and keywords that will help inspire the design:

Premium Health Insurance
Executive Health Insurance
Concierge Medicine
24/7 access dedicated concierge team
Integrative Concierge Care

I will upload logo files below, here are the font & colors information:

Font: Trajan Pro Bold
Colors:
Blue: hex code: 0071BD, Rgb code: 0, 113, 189  cmyk code: 87,53,0,0
Gray: hex code: #666666, Rgb code: 102,102,102 cmyk code: 60,51,51,20

```html
<!DOCTYPE html>
<html lang="en">
<head>
<meta charset="utf-8">
<title>Vantor Insurance Services</title>
<link rel="stylesheet" href="https://fonts.googleapis.com/css2?family=Poppins:wght@600;700&family=Lato:wght@400;700&display=swap">
<style>
:root{
  --blue:#0071bd;
  --blue-light:#e3eef8;
  --ink:#111111;
  --gray:#666666;
  --soft:#f3f5f7;
  --line:#d6dde4;
}
*{box-sizing:border-box;margin:0;padding:0}
html,body{width:1200px;height:4437px;overflow:hidden;background:#fff}
body{position:relative;font-family:"Lato",sans-serif;color:var(--ink)}
.abs{position:absolute}
h1,h2{font-family:"Poppins",sans-serif;font-weight:700;color:var(--ink);line-height:1.05}
.photo{position:absolute;border-radius:6px}
.brand{left:46px;top:24px;font-size:23px;font-weight:400;z-index:4}
.nav{top:28px;font-size:15px;z-index:4;white-space:nowrap;display:flex;align-items:center}
.btn{position:absolute;background:var(--blue);color:#fff;display:flex;align-items:center;justify-content:center;font-size:15px}
.header-btn{z-index:4}
.dropdown{left:706px;top:69px;width:207px;height:103px;background:#fff;box-shadow:0 4px 16px rgba(0,0,0,.12);font-size:15px;z-index:4}
.dropdown div{padding:18px 16px 0}
.hero-pill{left:127px;top:110px;width:408px;height:76px;background:var(--blue-light);border-radius:40px}
.tag-dark{background:#2a2a2a;color:#fff;border-radius:30px;display:flex;align-items:center;justify-content:center;font-size:15px}
.body-text{font-size:19px;line-height:32px;color:#555}
.stat-card{left:783px;top:441px;width:290px;height:148px;border-radius:10px;background:linear-gradient(160deg,#c9d0d8,#a9b3bf);border:3px solid #fff;box-shadow:0 4px 20px rgba(0,0,0,.12);z-index:2}
.avatar{position:absolute;border-radius:50%;background:linear-gradient(150deg,#c9a58f,#6f5448);border:2px solid #fff}
.feature h3{font-family:"Lato",sans-serif;font-weight:400;font-size:24px;line-height:29px}
.feature p{font-size:15px;line-height:22px;color:#555;margin-top:14px}
.feature .ic{position:absolute;left:-43px;top:-6px;width:46px;height:46px;border-radius:50%;background:#e9f1f9;display:flex;align-items:center;justify-content:center}
.checks li{list-style:none;position:relative;padding-left:50px;margin-bottom:14px;font-size:19px;line-height:26px;color:#555}
.checks li:before{content:"";position:absolute;left:26px;top:4px;width:5px;height:10px;border:solid var(--blue);border-width:0 2px 2px 0;transform:rotate(45deg)}
.card{background:var(--soft);border-radius:8px;width:302px;height:401px;top:2755px}
.card .photo{left:13px;top:14px;width:276px;height:167px}
.card .heart{position:absolute;left:222px;top:155px;width:54px;height:54px;border-radius:50%;background:var(--blue);border:4px solid #fff;display:flex;align-items:center;justify-content:center}
.card h3{position:absolute;left:13px;top:214px;font-weight:400;font-size:24px;line-height:29px;width:285px}
.card p{position:absolute;left:13px;top:285px;width:235px;font-size:15px;line-height:22.5px;color:#555}
.foot h4{font-family:"Poppins",sans-serif;font-weight:600;font-size:24px;line-height:29px}
.foot a{display:block;color:#555;text-decoration:none;font-size:15px;line-height:35px}
</style>
</head>
<body>

<!-- Hero image circle (behind header) -->
<div class="photo" role="img" aria-label="Close-up of an adult hand holding a baby's hand" style="left:689px;top:-155px;width:654px;height:654px;border-radius:50%;background:radial-gradient(circle at 45% 50%,#dcd4cc,#8ea1b1 70%,#6d8296);z-index:1"></div>

<!-- Header -->
<div class="abs brand">Vantor Insurance Services</div>
<div class="abs nav" style="left:558px">Health Insurance</div>
<div class="abs nav" style="left:704px">Services
  <svg width="14" height="10" viewBox="0 0 14 10" style="margin-left:6px"><path d="M2 8l5-5 5 5" fill="none" stroke="#111" stroke-width="1.6"/></svg>
</div>
<div class="btn header-btn" style="left:1050px;top:26px;width:104px;height:26px;border-radius:14px;font-size:13px">Get in Touch</div>
<div class="abs dropdown"><div>Concierge Medicine</div><div>Dental &amp; Vision</div></div>

<svg class="abs" style="left:0;top:0;z-index:0" width="1200" height="680">
  <path d="M0 90 C140 140 260 150 400 150" fill="none" stroke="#dfe3e7" stroke-width="1.5"/>
  <path d="M430 600 C560 580 680 540 783 520" fill="none" stroke="#cfd6dc" stroke-width="1.5" stroke-dasharray="8 8"/>
  <path d="M1073 580 C1090 600 1110 615 1130 630" fill="none" stroke="#cfd6dc" stroke-width="1.5"/>
</svg>
<div class="abs hero-pill">
  <div class="abs tag-dark" style="left:8px;top:19px;width:154px;height:38px">Tailored Solutions</div>
  <div class="abs" style="left:176px;top:6px;font-size:15px;line-height:21px">Experience Tailored<br>Healthcare with Vantor<br>Insurance Services ★</div>
</div>
<h1 class="abs" style="left:127px;top:212px;font-size:58px;line-height:58px">Premium<br>Healthcare<br>Insurance</h1>
<p class="abs body-text" style="left:127px;top:408px;width:460px">Elevate your health with customized insurance plans and concierge services designed for your unique lifestyle.</p>
<div class="btn" style="left:127px;top:537px;width:183px;height:54px;border-radius:4px">Discover Our Services</div>
<div class="avatar" role="img" aria-label="Portrait of a smiling client" style="left:367px;top:565px;width:76px;height:76px"></div>
<div class="abs stat-card">
  <div class="avatar" role="img" aria-label="Client portrait" style="left:28px;top:30px;width:32px;height:32px"></div>
  <div class="avatar" role="img" aria-label="Client portrait" style="left:52px;top:30px;width:32px;height:32px"></div>
  <div class="avatar" role="img" aria-label="Client portrait" style="left:76px;top:30px;width:32px;height:32px"></div>
  <div class="avatar" role="img" aria-label="Client portrait" style="left:100px;top:30px;width:32px;height:32px"></div>
  <div class="avatar" role="img" aria-label="Client portrait" style="left:124px;top:30px;width:32px;height:32px"></div>
  <div class="abs" style="left:26px;top:84px;color:#fff;font-size:27px;white-space:nowrap">5,000+ <span style="font-size:19px">Satisfied Clients</span></div>
</div>

<!-- Bespoke intro -->
<div class="abs" style="left:86px;top:699px;width:1028px;height:193px;background:var(--blue-light);border-radius:14px"></div>
<svg class="abs" style="left:138px;top:913px" width="240" height="240"><circle cx="120" cy="120" r="107" fill="none" stroke="var(--blue)" stroke-width="26"/></svg>
<div class="photo" role="img" aria-label="Doctor touching a digital health shield interface" style="left:38px;top:752px;width:251px;height:367px;background:linear-gradient(160deg,#cfe3f6,#5ea1d9 55%,#a7c3dc);border:3px solid #fff;box-shadow:0 4px 14px rgba(0,0,0,.12)"></div>
<div class="photo" role="img" aria-label="Scientist in a lab coat working in a laboratory" style="left:320px;top:752px;width:252px;height:367px;background:linear-gradient(170deg,#20324f,#6d8fb4 50%,#1c2940)"></div>
<h2 class="abs" style="left:625px;top:750px;font-size:40px;line-height:48px">Bespoke Concierge<br>Services</h2>
<p class="abs body-text" style="left:625px;top:862px;width:405px">Experience unparalleled health insurance and concierge medicine tailored specifically for affluent individuals and families, ensuring you receive a level of care that reflects your unique needs.</p>
<div class="abs" style="left:625px;top:1050px;width:408px;height:90px;background:var(--soft);border-radius:45px">
  <div class="abs" style="left:27px;top:18px;color:var(--blue);font-size:18px;line-height:26px;width:330px"><span style="font-size:27px">10+</span>&nbsp; Years of Supporting Affluent Clients</div>
</div>
<svg class="abs" style="left:1030px;top:870px" width="170" height="280"><path d="M170 10 C80 60 40 150 60 270" fill="none" stroke="#dfe3e7" stroke-width="1.5"/></svg>

<!-- Headline row -->
<h2 class="abs" style="left:127px;top:1337px;font-size:38px;line-height:40px">Premium<br>Healthcare</h2>
<div class="abs tag-dark" style="left:446px;top:1345px;width:262px;height:64px;font-family:Poppins,sans-serif;font-weight:600;font-size:19px;line-height:25px;text-align:center">Bespoke Concierge<br>Services</div>
<h2 class="abs" style="left:716px;top:1337px;font-size:38px;line-height:40px">Absolute Peace of<br>Mind.</h2>

<!-- Features band -->
<div class="abs" role="img" aria-label="Soft-focus photo of a consultation in a medical office" style="left:0;top:1477px;width:1200px;height:403px;background:linear-gradient(90deg,#c9ced3,#eef0f2 30%,#e4e7ea 70%,#bcc2c8)"></div>
<div class="abs" style="left:127px;top:1477px;width:947px;height:326px;background:#fff;border-radius:0 0 6px 6px"></div>
<svg class="abs" style="left:203px;top:1535px" width="460" height="250">
  <line x1="0" y1="0" x2="0" y2="90" stroke="#d6dde4" stroke-dasharray="4 6"/>
  <line x1="0" y1="160" x2="0" y2="250" stroke="#d6dde4" stroke-dasharray="4 6"/>
  <line x1="437" y1="0" x2="437" y2="45" stroke="#d6dde4" stroke-dasharray="4 6"/>
</svg>
<div class="abs feature" style="left:246px;top:1487px;width:345px">
  <div class="ic"><svg width="16" height="16" viewBox="0 0 16 16"><circle cx="8" cy="5" r="3" fill="var(--blue)"/><path d="M2 15c0-4 3-6 6-6s6 2 6 6z" fill="var(--blue)"/></svg></div>
  <h3>Comprehensive Health<br>Solutions</h3>
  <p>Discover premium health insurance options tailored specifically for affluent individuals, ensuring peace of mind.</p>
</div>
<div class="abs feature" style="left:680px;top:1487px;width:345px">
  <div class="ic"><svg width="16" height="16" viewBox="0 0 16 16"><path d="M3 9a5 5 0 0 1 10 0" fill="none" stroke="var(--blue)" stroke-width="2"/><rect x="2" y="8" width="3" height="5" rx="1" fill="var(--blue)"/><rect x="11" y="8" width="3" height="5" rx="1" fill="var(--blue)"/></svg></div>
  <h3>24/7 Concierge Access</h3>
  <p>Benefit from 24/7 access to a dedicated concierge team, ensuring your health needs are met with utmost convenience.</p>
</div>
<div class="abs feature" style="left:246px;top:1651px;width:345px">
  <div class="ic"><svg width="16" height="16" viewBox="0 0 16 16"><path d="M8 1l6 2v5c0 4-3 6-6 7-3-1-6-3-6-7V3z" fill="var(--blue)"/></svg></div>
  <h3>Exclusive Membership Benefits</h3>
  <p>Unlock tailored offers and promotions designed specifically for our VIP clients, enhancing your healthcare experience.</p>
</div>
<div class="abs feature" style="left:680px;top:1651px;width:345px">
  <div class="ic"><svg width="18" height="16" viewBox="0 0 18 16"><ellipse cx="7" cy="6" rx="6" ry="4.5" fill="var(--blue)"/><ellipse cx="12" cy="10" rx="5" ry="4" fill="var(--blue)" opacity=".8"/></svg></div>
  <h3>Client-Centric Feedback Loop</h3>
  <p>We value your input. Share your experiences to help us enhance our offerings and provide an unmatched experience.</p>
</div>

<!-- Peace of mind -->
<h2 class="abs" style="left:127px;top:1908px;font-size:38px;line-height:40px">Absolute Peace of<br>Mind.</h2>
<p class="abs" style="left:127px;top:2032px;width:460px;font-size:19px;line-height:26px;color:#555">Experience unparalleled health solutions tailored for affluent families, ensuring every aspect of your healthcare journey is meticulously designed for your needs.</p>
<ul class="abs checks" style="left:127px;top:2163px;width:465px">
  <li>Tailored Health Insurance - Our exclusive plans offer coverage that reflects your lifestyle and requirements.</li>
  <li>24/7 Concierge Access - Enjoy immediate assistance from our dedicated team, available at all times to address your health needs.</li>
  <li>Personalized Care Experience - Our concierge medicine ensures that you receive individualized attention and care, right in the comfort of your home.</li>
</ul>
<p class="abs" style="left:127px;top:2472px;width:450px;font-size:19px;line-height:26px;color:#555">Elevate your healthcare experience with Vantor Insurance Services, where your health is our highest priority.</p>
<div class="abs" style="left:610px;top:1880px;width:470px;height:470px;border-radius:50%;background:radial-gradient(circle,#e6f0fa,rgba(255,255,255,0) 70%)"></div>
<div class="photo" role="img" aria-label="Hands typing on a laptop with digital insurance and health icons" style="left:663px;top:1913px;width:358px;height:389px;background:linear-gradient(160deg,#e7edf3,#b9c8d6 55%,#56657a);border:3px solid #fff;box-shadow:0 4px 14px rgba(0,0,0,.1)"></div>

<!-- Services cards -->
<h2 class="abs" style="left:127px;top:2600px;font-size:38px;line-height:39px">Bespoke<br>Concierge<br>Services</h2>
<p class="abs" style="left:608px;top:2606px;width:465px;font-size:19px;line-height:26px;color:#555">Indulge in luxurious health insurance solutions and tailored concierge services that offer unparalleled peace of mind for high-net-worth individuals and their families.</p>
<div class="abs card" style="left:127px">
  <div class="photo" role="img" aria-label="Hands signing an insurance document beside a stethoscope" style="background:linear-gradient(160deg,#eef0f2,#b8bcc0 60%,#6e5a4d)"></div>
  <div class="heart"><svg width="20" height="18" viewBox="0 0 20 18"><path d="M10 17S1 11 1 5.5A4.5 4.5 0 0 1 10 3a4.5 4.5 0 0 1 9 2.5C19 11 10 17 10 17z" fill="#fff"/></svg></div>
  <h3>Tailored Health Insurance Plans</h3>
  <p>Experience comprehensive coverage crafted to meet the exclusive needs of affluent families, ensuring optimal health without compromise.</p>
</div>
<div class="abs card" style="left:449px">
  <div class="photo" role="img" aria-label="Hand stacking wooden blocks with health icons" style="background:linear-gradient(160deg,#4d86bf,#9cc0e0 55%,#c9a67d)"></div>
  <div class="heart"><svg width="20" height="18" viewBox="0 0 20 18"><path d="M10 17S1 11 1 5.5A4.5 4.5 0 0 1 10 3a4.5 4.5 0 0 1 9 2.5C19 11 10 17 10 17z" fill="#fff"/></svg></div>
  <h3>Exclusive Concierge Medicine</h3>
  <p>Access your private physician 24/7, ensuring that personalized medical care is always available right at your home.</p>
</div>
<div class="abs card" style="left:771px">
  <div class="photo" role="img" aria-label="Person writing notes at a desk" style="background:linear-gradient(160deg,#e5e3e0,#c6bfb7 55%,#7d6a5d)"></div>
  <div class="heart"><svg width="20" height="18" viewBox="0 0 20 18"><path d="M10 17S1 11 1 5.5A4.5 4.5 0 0 1 10 3a4.5 4.5 0 0 1 9 2.5C19 11 10 17 10 17z" fill="#fff"/></svg></div>
  <h3>Premium Dental &amp; Vision Coverage</h3>
  <p>Protect your smile and vision with our bespoke plans, ensuring that your health needs are perfectly catered to with the utmost precision.</p>
</div>

<!-- CTA -->
<div class="abs" role="img" aria-label="Desk with laptop, clipboard and smartphone" style="left:0;top:3208px;width:1200px;height:274px;background:linear-gradient(90deg,#b9c3cc,#e4e9ee 35%,#eef1f4 60%,#c3ccd4)"></div>
<h2 class="abs" style="left:0;top:3270px;width:1200px;text-align:center;font-size:38px;line-height:40px;font-weight:600">Let's Talk About our Offer for<br>Seniors</h2>
<div class="btn" style="left:544px;top:3379px;width:112px;height:51px;border-radius:26px">Call Us Now</div>

<!-- Testimonials -->
<h2 class="abs" style="left:127px;top:3559px;font-size:38px;line-height:40px;font-weight:600">Testimonials from<br>Our Valued Clients</h2>
<p class="abs" style="left:127px;top:3665px;width:420px;font-size:19px;line-height:32px;color:#555">“Vantor Insurance Services has significantly elevated my healthcare journey. Their bespoke concierge approach and 24/7 availability to my personal physician provide reassurance that my health needs are met promptly and effectively.”</p>
<div class="abs" style="left:127px;top:3845px;width:412px;height:2px;background:#888"></div>
<div class="abs" style="left:127px;top:3870px;font-size:24px;line-height:28px;width:420px">Daniel Whitmore - High Net-Worth<br>Client</div>
<svg class="abs" style="left:640px;top:3490px" width="560" height="600">
  <ellipse cx="380" cy="230" rx="330" ry="200" fill="none" stroke="#d6dde4" stroke-width="1.5" stroke-dasharray="10 10" transform="rotate(-20 380 230)"/>
  <ellipse cx="380" cy="230" rx="230" ry="140" fill="none" stroke="#d6dde4" stroke-width="1.5" stroke-dasharray="10 10" transform="rotate(-20 380 230)"/>
</svg>
<div class="abs" style="left:930px;top:3670px;transform:rotate(6deg);text-align:center">
  <div style="font-family:Poppins,sans-serif;font-weight:600;font-size:60px;line-height:60px">25K</div>
  <div style="font-size:25px;color:#444">Satisfied Clients</div>
</div>
<div class="avatar" role="img" aria-label="Client portrait" style="left:918px;top:3515px;width:82px;height:82px;border:4px solid #fff;box-shadow:0 3px 10px rgba(0,0,0,.15)"></div>
<div class="avatar" role="img" aria-label="Client portrait" style="left:666px;top:3630px;width:86px;height:86px;background:linear-gradient(150deg,#f3a3a0,#c46a5d);border:4px solid #fff;box-shadow:0 3px 10px rgba(0,0,0,.15)"></div>
<div class="avatar" role="img" aria-label="Client portrait" style="left:978px;top:3914px;width:94px;height:94px;background:linear-gradient(150deg,#5e6e80,#2b3440);border:4px solid #fff;box-shadow:0 3px 10px rgba(0,0,0,.15)"></div>

<!-- Footer -->
<div class="abs foot" style="left:128px;top:4130px;width:230px">
  <h4>Vantor Insurance<br>Services</h4>
  <p style="margin-top:26px;font-size:15px;line-height:23px;color:#222">Specializing in Health Insurance and Concierge Medicine for high net-worth individuals. Experience absolute peace of mind.</p>
</div>
<div class="abs foot" style="left:420px;top:4130px">
  <h4>Explore</h4>
  <div style="margin-top:14px"><a>Home</a><a>Health Insurance</a><a>Concierge Medicine</a><a>Dental &amp; Vision</a></div>
</div>
<div class="abs foot" style="left:625px;top:4130px">
  <h4>Our Services</h4>
  <div style="margin-top:14px"><a>Premium Health Insurance</a><a>Executive Health Insurance</a><a>Concierge Medicine</a><a>Integrative Concierge Care</a></div>
</div>
<div class="abs" style="left:128px;top:4394px;font-size:15px">Copyright © 2025 Vantor Insurance Services.</div>

</body>
</html>
```